Investor Presentation

We have a deck that is mostly finished that needs to be properly formatted and cleaned up. The presentation is for an investment in a financial firm. So the design we are looking for is very professional and minimalistic. A very clean look with conservative color schemes and fonts. The designer can leverage our existing logos, background, etc.

The final design files should have full editing functionality.

Target Market(s)

Sophisticated institutional investors

Industry/Entity Type

Conservative

Requirements
Nice to have
• Cleaned up / formatted tables from the attached files to add to the presentation.

```html
<!DOCTYPE html>
<html lang="en">
<head>
<meta charset="utf-8">
<title>Table data Heading</title>
<link href="https://fonts.googleapis.com/css2?family=Roboto:wght@400;700&family=Ubuntu:wght@400;500&display=swap" rel="stylesheet">
<style>
  :root {
    --teal-dark: #02747a;
    --teal-footer: #3596a2;
    --teal-text: #0b7379;
    --body-text: #333333;
    --white: #ffffff;
  }
  html, body {
    margin: 0;
    padding: 0;
    overflow: hidden;
    background: var(--white);
  }
  .slide {
    position: relative;
    width: 1200px;
    height: 900px;
    overflow: hidden;
    background: var(--white);
    font-family: "Roboto", Arial, sans-serif;
  }
  .slide-header {
    position: absolute;
    left: 0;
    top: 0;
    width: 1200px;
    height: 99px;
    background: var(--teal-dark);
  }
  .slide-title {
    position: absolute;
    left: 27px;
    top: 24px;
    margin: 0;
    font-family: "Ubuntu", Arial, sans-serif;
    font-weight: 400;
    font-size: 42px;
    line-height: 52px;
    color: var(--white);
  }
  .brand {
    position: absolute;
    right: 15px;
    top: 44px;
    display: flex;
    align-items: center;
    gap: 12px;
    font-family: "Ubuntu", Arial, sans-serif;
    font-size: 24px;
    line-height: 28px;
    color: var(--white);
  }
  .brand-mark {
    width: 22px;
    height: 22px;
    border-radius: 50%;
    background: var(--white);
  }
  .column {
    position: absolute;
    top: 214px;
    width: 470px;
  }
  .column-left { left: 75px; }
  .column-right { left: 632px; }
  .column-subtitle {
    margin: 0;
    font-weight: 700;
    font-size: 24px;
    line-height: 32px;
    color: var(--teal-text);
  }
  .column-text {
    position: absolute;
    left: 0;
    margin: 0;
    font-size: 17.5px;
    line-height: 30px;
    color: var(--body-text);
    white-space: nowrap;
  }
  .text-first { top: 45px; }
  .text-second { top: 261px; }
  .text-third { top: 395px; }
  .slide-footer {
    position: absolute;
    left: 0;
    bottom: 0;
    width: 1200px;
    height: 43px;
    background: var(--teal-footer);
  }
  .copyright {
    position: absolute;
    left: 12px;
    top: 10px;
    margin: 0;
    font-family: "Ubuntu", Arial, sans-serif;
    font-size: 19px;
    line-height: 24px;
    color: var(--white);
  }
</style>
</head>
<body>
<div class="slide">
  <header class="slide-header">
    <h1 class="slide-title">Table data Heading</h1>
    <div class="brand"><span class="brand-mark"></span><span class="brand-name">Harlow Crest Partners, LLC</span></div>
  </header>

  <section class="column column-left">
    <h2 class="column-subtitle">Paragraph Subtitle Here</h2>
    <p class="column-text text-first">Lorem ipsum dolor sit Lorem ipsum dolor sit&nbsp; Lorem<br>ipsum dolor sit Lorem ipsum dolor sit&nbsp; Lorem ipsum<br>dolor sit Lorem ipsum dolor sit&nbsp; Lorem ipsum dolor sit<br>Lorem ipsum dolor sit&nbsp; Lorem ipsum dolor sit Lorem<br>ipsum dolor sit&nbsp; Lorem ipsum dolor sit Lorem ipsum<br>dolor sit&nbsp; Lorem ipsum dolor sit Lorem ipsum dolor sit<br>Lorem ipsum dolor sit Lorem ipsum dolor sit</p>
    <p class="column-text text-second">Lorem ipsum dolor sit Lorem ipsum dolor sit&nbsp; Lorem<br>ipsum dolor sit Lorem ipsum dolor sit&nbsp; Lorem ipsum<br>dolor sit Lorem ipsum dolor sit&nbsp; Lorem ipsum dolor</p>
    <p class="column-text text-third">Lorem ipsum dolor sit Lorem ipsum dolor sit&nbsp; Lorem<br>ipsum dolor sit Lorem ipsum dolor sit&nbsp; Lorem ipsum<br>dolor sit Lorem ipsum dolor sit&nbsp; Lorem ipsum dolor</p>
  </section>

  <section class="column column-right">
    <h2 class="column-subtitle">Paragraph Subtitle Here</h2>
    <p class="column-text text-first">Lorem ipsum dolor sit Lorem ipsum dolor sit&nbsp; Lorem<br>ipsum dolor sit Lorem ipsum dolor sit&nbsp; Lorem ipsum<br>dolor sit Lorem ipsum dolor sit&nbsp; Lorem ipsum dolor sit<br>Lorem ipsum dolor sit&nbsp; Lorem ipsum dolor sit Lorem<br>ipsum dolor sit&nbsp; Lorem ipsum dolor sit Lorem ipsum<br>dolor sit&nbsp; Lorem ipsum dolor sit Lorem ipsum dolor sit<br>Lorem ipsum dolor sit Lorem ipsum dolor sit</p>
    <p class="column-text text-second">Lorem ipsum dolor sit Lorem ipsum dolor sit&nbsp; Lorem<br>ipsum dolor sit Lorem ipsum dolor sit&nbsp; Lorem ipsum<br>dolor sit Lorem ipsum dolor sit&nbsp; Lorem ipsum dolor</p>
    <p class="column-text text-third">Lorem ipsum dolor sit Lorem ipsum dolor sit&nbsp; Lorem<br>ipsum dolor sit Lorem ipsum dolor sit&nbsp; Lorem ipsum<br>dolor sit Lorem ipsum dolor sit&nbsp; Lorem ipsum dolor</p>
  </section>

  <footer class="slide-footer">
    <p class="copyright">Copyright text here</p>
  </footer>
</div>
</body>
</html>
```